Ostrel Appraisals BV business cards (a financial services company)

I am looking for a business card design that stands out in the financial advisory field of business & intellectual property valuation. The business card design should be conservative, yet different. Address details have changed since the attached business card. New address is:

Molenvlietkade 27
4817 KT Leiden
The Netherlands

Telephone number remains the same.

```html
<!DOCTYPE html>
<html lang="en">
<head>
<meta charset="utf-8">
<title>Ostrel Appraisals BV – Business Cards</title>
<link rel="stylesheet" href="https://fonts.googleapis.com/css2?family=Montserrat:wght@400;500;600&display=swap">
<style>
  :root {
    --stage: #1d1d1d;
    --card-light: #f7f7f7;
    --card-dark: #111111;
    --ink-grey: #7a7a7a;
    --ink-mid: #9a9a9a;
    --ink-white: #f2f2f2;
    --rule: #5a5a5a;
    --icon-bg: #8c8c8c;
  }
  * { box-sizing: border-box; margin: 0; padding: 0; }
  html, body {
    width: 1200px; height: 1200px; overflow: hidden;
    background: var(--stage);
    font-family: "Montserrat", sans-serif;
  }
  .stage {
    position: relative; width: 1200px; height: 1200px;
  }
  .card {
    position: absolute; left: 180px; width: 840px; height: 480px;
    border-radius: 28px;
    box-shadow: 0 18px 40px rgba(0,0,0,0.55);
  }

  /* Front */
  .card--front {
    top: 90px; background: var(--card-light);
    display: flex; flex-direction: column; align-items: center;
  }
  .brand-front {
    margin-top: 120px;
    display: flex; align-items: center; gap: 16px;
    color: var(--ink-grey); font-weight: 500; font-size: 44px;
    letter-spacing: 1px; text-transform: uppercase;
  }
  .brand-mark {
    width: 22px; height: 22px; background: currentColor;
  }
  .tagline-front {
    margin-top: 22px; text-align: center; color: var(--ink-grey);
    text-transform: uppercase; font-weight: 600; line-height: 1.15;
  }
  .tagline-front .line1 { font-size: 20px; letter-spacing: 1px; }
  .tagline-front .line2 { font-size: 27px; letter-spacing: 1px; }
  .web-front {
    margin-top: 70px; color: var(--ink-grey); font-size: 16px;
    letter-spacing: 11px; text-transform: uppercase; font-weight: 500;
  }

  /* Back */
  .card--back {
    top: 620px; background: var(--card-dark); color: var(--ink-white);
  }
  .brand-back {
    position: absolute; left: 56px; top: 70px;
    display: flex; align-items: center; gap: 12px;
    font-size: 28px; font-weight: 500; text-transform: uppercase;
    letter-spacing: 0.5px; color: var(--ink-white);
  }
  .brand-back .brand-mark { width: 16px; height: 16px; }
  .tagline-back {
    position: absolute; right: 56px; top: 64px; text-align: right;
    text-transform: uppercase; font-weight: 600; line-height: 1.2;
  }
  .tagline-back .line1 { font-size: 15px; color: var(--ink-mid); letter-spacing: 0.5px; }
  .tagline-back .line2 { font-size: 20px; color: var(--ink-white); letter-spacing: 0.5px; }
  .address {
    position: absolute; right: 56px; top: 140px; text-align: right;
    font-style: normal; font-size: 17px; line-height: 1.6; letter-spacing: 0.5px;
  }
  .divider {
    position: absolute; left: 56px; right: 56px; top: 262px;
    height: 1px; background: var(--rule);
  }
  .person { position: absolute; left: 56px; top: 282px; text-transform: uppercase; }
  .person-name { font-size: 22px; font-weight: 600; letter-spacing: 0.5px; }
  .person-role { font-size: 17px; color: var(--ink-grey); letter-spacing: 0.5px; margin-top: 2px; }
  .contacts {
    position: absolute; right: 56px; top: 346px; list-style: none;
    font-size: 17px; letter-spacing: 0.5px; line-height: 1;
  }
  .contacts li {
    display: flex; justify-content: flex-end; align-items: center; gap: 12px;
    margin-bottom: 8px;
  }
  .icon {
    width: 24px; height: 24px; border-radius: 5px; background: var(--icon-bg);
    display: flex; align-items: center; justify-content: center;
  }
  .icon svg { width: 15px; height: 15px; }
</style>
</head>
<body>
<main class="stage">

  <section class="card card--front" aria-label="Card front">
    <div class="brand-front"><span class="brand-mark"></span>Ostrel Appraisals</div>
    <div class="tagline-front">
      <div class="line1">Business and Intellectual</div>
      <div class="line2">Property Valuations</div>
    </div>
    <div class="web-front">www.ostrelappraisals.com</div>
  </section>

  <section class="card card--back" aria-label="Card back">
    <div class="brand-back"><span class="brand-mark"></span>Ostrel Appraisals</div>

    <div class="tagline-back">
      <div class="line1">Business and Intellectual</div>
      <div class="line2">Property Valuations</div>
    </div>

    <address class="address">
      Molenvlietkade 27<br>
      4817 KT Leiden<br>
      The Netherlands
    </address>

    <div class="divider"></div>

    <div class="person">
      <div class="person-name">Marten Vos, CFA, ASA, RV</div>
      <div class="person-role">Managing Director</div>
    </div>

    <ul class="contacts">
      <li>+31 (0)70 418 2736
        <span class="icon"><svg viewBox="0 0 24 24" fill="#fff"><path d="M6.6 10.8a15.1 15.1 0 0 0 6.6 6.6l2.2-2.2c.3-.3.7-.4 1-.2 1.1.4 2.3.6 3.6.6.6 0 1 .4 1 1V20c0 .6-.4 1-1 1A17 17 0 0 1 3 4c0-.6.4-1 1-1h3.5c.6 0 1 .4 1 1 0 1.3.2 2.5.6 3.6.1.3 0 .7-.2 1l-2.3 2.2z"/></svg></span>
      </li>
      <li>mvos@ostrelappraisals.com
        <span class="icon"><svg viewBox="0 0 24 24" fill="none" stroke="#fff" stroke-width="2"><rect x="3" y="5" width="18" height="14" rx="1"/><path d="M3 6l9 7 9-7"/></svg></span>
      </li>
      <li>www.ostrelappraisals.com
        <span class="icon"><svg viewBox="0 0 24 24" fill="none" stroke="#fff" stroke-width="1.8"><circle cx="12" cy="12" r="9"/><path d="M3 12h18M12 3c3 3 3 15 0 18M12 3c-3 3-3 15 0 18"/></svg></span>
      </li>
    </ul>
  </section>

</main>
</body>
</html>
```